Professional Home Buyer business card needed

I need a pretty straight forward business card designed. We help people that NEED to sell their homes solve problems. We perform all types of Real Estate transactions including flip, wholesale, investment, rental property and multi family. The card will mainly be used to give to prospective Sellers but will also be given to Real Estate Investors as well. It should professional and very easy to read, most clients are older people.

Target Market(s)

Distressed home sellers as well as Real Estate investors

Industry/Entity Type

Real Estate

Contact Information for Business Card

should be a professional layout

Colors
ec1f27
ffffff
000000

Requirements
Must have
• Large logo on back and smaller one on front. should utilize Red, white, and black.
• I am thinking of using a soft touch coating on the card so keep that in mind.
• Contact info should be very easy to read, think older clients.
Nice to have
• I would like to see a design with rounded corners on the card
Should not have
• pictures of homes or other home graphics.

```html
<!DOCTYPE html>
<html lang="en">
<head>
<meta charset="utf-8">
<title>Kestrel Home Buyers – Business Card</title>
<link rel="stylesheet" href="https://fonts.googleapis.com/css2?family=Roboto:wght@400;500;900&display=swap">
<style>
  :root {
    --red: #ec1f27;
    --white: #ffffff;
    --black: #000000;
    --card-black: #111111;
    --backdrop: #2a2a2a;
  }
  * { box-sizing: border-box; margin: 0; padding: 0; }
  html, body {
    width: 1200px; height: 900px; overflow: hidden;
    background: var(--backdrop);
    font-family: "Roboto", Arial, sans-serif;
  }
  .stage {
    position: relative; width: 1200px; height: 900px;
    display: flex; justify-content: center; align-items: center; gap: 100px;
  }
  .card {
    position: relative; width: 360px; height: 630px;
    border-radius: 16px; overflow: hidden;
    box-shadow: 0 18px 40px rgba(0,0,0,.45);
  }
  .card-front { background: var(--card-black); }
  .front-backdrop { position: absolute; inset: 0; }
  .brand {
    position: absolute; left: 0; right: 0;
    text-align: center; font-weight: 900; text-transform: uppercase;
    letter-spacing: 2px; line-height: 1.05;
  }
  .card-front .brand {
    top: 120px; color: var(--black); font-size: 40px;
  }
  .brand-sub { display: block; font-size: .55em; letter-spacing: 6px; margin-top: 8px; }
  .contact {
    position: absolute; left: 0; right: 0; top: 350px;
    text-align: center; color: var(--white);
  }
  .contact-name { color: var(--red); font-size: 30px; font-weight: 400; letter-spacing: .5px; }
  .contact-title { font-size: 21px; margin-top: 4px; }
  .contact-phone { font-size: 32px; font-weight: 500; margin-top: 26px; letter-spacing: .5px; }
  .contact-line { font-size: 17px; margin-top: 8px; }
  .contact-address { font-size: 19px; margin-top: 18px; line-height: 1.3; }

  .card-back {
    background: linear-gradient(160deg, #1a1a1a 0%, var(--card-black) 55%, #171717 100%);
  }
  .card-back .brand {
    top: 255px; color: var(--white); font-size: 50px;
  }
  .card-back .brand-sub { font-size: .5em; margin-top: 12px; }
  .back-rule {
    position: absolute; left: 60px; right: 60px; top: 240px; height: 3px; background: var(--red);
  }
  .back-rule.bottom { top: 392px; }
</style>
</head>
<body>
<main class="stage">
  <section class="card card-front" aria-label="Card front">
    <svg class="front-backdrop" width="360" height="630" viewBox="0 0 360 630" aria-hidden="true">
      <path d="M0 0 H360 V255 Q180 300 0 340 Z" fill="var(--white)"/>
      <path d="M0 340 Q180 300 360 255" fill="none" stroke="var(--red)" stroke-width="5"/>
    </svg>
    <h1 class="brand">Kestrel<span class="brand-sub">Home Buyers</span></h1>
    <div class="contact">
      <p class="contact-name">DANA WHITLOW</p>
      <p class="contact-title">President</p>
      <p class="contact-phone">555-014-2286</p>
      <p class="contact-line">dana@prairiehomesforcash.com</p>
      <p class="contact-line">www.prairiehomesforcash.com</p>
      <p class="contact-address">P.O. Box 18<br>Millbrook, KS 67000</p>
    </div>
  </section>

  <section class="card card-back" aria-label="Card back">
    <div class="back-rule"></div>
    <h2 class="brand">Kestrel<span class="brand-sub">Home Buyers</span></h2>
    <div class="back-rule bottom"></div>
  </section>
</main>
</body>
</html>
```